Book cover for a book on tactics, habits and directives learned from world class performers

The Quiet Ledger book is the first in a series of four books filled with proven tactics, habits and directives (i.e., what to do) that young, ambitious working professionals should be doing to make their life better. The first book is on foundational or keystone habits - that is, the habits that will help everyone upgrade their life and enable other great habits in their life (things such as waking up early in the morning or exercising)

The goal of the book is to stand out on the Brimvale platform as a small thumbnail, as well as a 5 x 8 book.

The imagery should make the viewer feel that the book (and the author) are the authority in habits and developing habits.

The reader should feel that they must have this book if they know they should be developing successful habits but do not want to comb through hundreds of books just to find the one tactic or habit that they should be doing. It's important that the book "pops off the shelf" and catches the eye quickly.

The most important part of the design is that it sells, not that it looks well-designed. I am open to any image or illustration you choose though please consider the nice have I have listed below. Here are a few words that come to mind when thinking of my book: growth, self development, leadership, success, freedom, passion, motivation, young professional, accomplished, experience.

I like a bold color palette. I like bold titles that you know right away what the title is and what it is about, not too busy and with simple color schemes. 2 - 3 colors.

Books with covers I like:
- Lamp Orchard by Norris Pellaquin
- Under The Copper Tide by Gordon Pruitt
- The Velvet Compass by Edgar Fulbright

Target Market(s)

- Young 20 - 40 year old ambitious working professionals interested in self development and listen to podcasts of Ned Caplow, Rufus Denholme
- Just starting out management consultants

Colors

Designer to choose colors to be used in the design.

Requirements
Must have
• 'Quiet Ledger' title - first and foremost
• Author name - Lu Qiao - probably on the bottom or somewhere
• Bold colour / colours or a graphic that is eye catching (and makes it different from other habits books on Brimvale)
Nice to have
• Would like to have some sort of visual, colour or theme that can run through the four books - would be great to have a cover design that can be simply changed to depict the second, third or fourth book in the series - maybe the graphic or visual can be changed with some colours, etc. but with the overall feel looking similar so that people can see that it's part of the same book series

```html
<!DOCTYPE html>
<html lang="en">
<head>
<meta charset="utf-8">
<title>Quiet Ledger — Lu Qiao</title>
<link rel="stylesheet" href="https://fonts.googleapis.com/css2?family=Anton&family=Montserrat:wght@500&display=swap">
<style>
  :root {
    --cover-blue: #3e4f95;
    --doodle-blue: #6c7cc0;
    --doodle-light: #a9b4e2;
    --banner-white: #f7f8fc;
    --title-orange: #f3801f;
    --title-shadow: #2c3a73;
  }
  html, body {
    margin: 0;
    padding: 0;
    overflow: hidden;
    background: var(--cover-blue);
  }
  .cover {
    position: relative;
    width: 800px;
    height: 1200px;
    background: var(--cover-blue);
    overflow: hidden;
  }
  .doodle-field {
    position: absolute;
    border-radius: 24px;
    background: radial-gradient(ellipse at center, var(--doodle-light) 0%, var(--doodle-blue) 55%, rgba(108,124,192,0) 78%);
    opacity: 0.75;
  }
  .doodle-field--top { left: 20px; top: 40px; width: 760px; height: 330px; }
  .doodle-field--bottom { left: 40px; top: 390px; width: 740px; height: 220px; }
  .banner {
    position: absolute;
    background: var(--banner-white);
    box-shadow: 0 4px 0 rgba(0,0,0,0.15);
  }
  .banner--first { left: 53px; top: 150px; width: 680px; height: 130px; transform: skewY(-1.5deg); }
  .banner--second { left: 160px; top: 430px; width: 613px; height: 130px; transform: skewY(-1deg); }
  .title-word {
    position: absolute;
    margin: 0;
    font-family: "Anton", "Impact", sans-serif;
    font-weight: 400;
    color: var(--title-orange);
    text-transform: uppercase;
    letter-spacing: 2px;
    line-height: 1;
    text-shadow: 4px 4px 0 var(--title-shadow);
    -webkit-text-stroke: 3px var(--banner-white);
    paint-order: stroke fill;
  }
  .title-word--first { left: 60px; top: 160px; font-size: 112px; }
  .title-word--second { left: 330px; top: 440px; font-size: 112px; }
  .figure-art {
    position: absolute;
    left: 590px; top: 150px;
    width: 150px; height: 160px;
    border-radius: 12px;
    background: linear-gradient(160deg, #31406f, #1f2a52);
  }
  .clock-art {
    position: absolute;
    left: 147px; top: 390px;
    width: 165px; height: 185px;
    border-radius: 50%;
    background: radial-gradient(circle, #ffffff 0%, #e7eaf5 45%, #2c3a73 62%, #2c3a73 100%);
  }
  .author {
    position: absolute;
    left: 0; right: 0;
    top: 1070px;
    margin: 0;
    text-align: center;
    font-family: "Montserrat", "Helvetica", sans-serif;
    font-weight: 500;
    font-size: 38px;
    letter-spacing: 10px;
    color: var(--title-orange);
    text-transform: uppercase;
  }
</style>
</head>
<body>
  <main class="cover">
    <div class="doodle-field doodle-field--top" role="img" aria-label="Scattered white hand-drawn doodles of charts, arrows and icons"></div>
    <div class="doodle-field doodle-field--bottom" role="img" aria-label="Scattered white hand-drawn doodles of charts, arrows and icons"></div>

    <div class="banner banner--first"></div>
    <h1 class="title-word title-word--first">Quiet</h1>
    <div class="figure-art" role="img" aria-label="Silhouette of a person stretching in an exercise pose"></div>

    <div class="banner banner--second"></div>
    <div class="clock-art" role="img" aria-label="Illustration of a classic twin-bell alarm clock"></div>
    <h2 class="title-word title-word--second">Ledger</h2>

    <p class="author">Lu Qiao</p>
  </main>
</body>
</html>
```